Introducing a Personal Care Product called" ORBA"

We are a nutra-pharmaceutical company launching a new personal care product called ORBA. Some of the products include massage and aroma therapy, as well as personal lubricants. The products will be produced and put into, two bottles that are interlocking so two combinations of products can be purchased at once (i.e. massage and aroma therapy). The poster will be used for promotional advertising, trade shows and for in-store promotions.
Updates

We would like to see a design without the product.

Target Market(s)

Products will be aimed at adults primarily women 18-65 in the USA. We want to appeal to the everyday woman who is interested in their sexual well being.

Industry/Entity Type

Massage

Requirements
Must have
• Clean Presentation. Not many colors. Text should be as follows: ORBA for Her....ORBA for Him...ORBA for You...Let's ORBA see attached..Also ORBA with Her...Orba with Him..Let's ORBA..Open to other copy versions.
Nice to have
• Product image not necessary but can be used. image attached
Should not have
• Too many colors...

```html
<!DOCTYPE html>
<html lang="en">
<head>
<meta charset="UTF-8">
<title>Let's Lunae — Poster</title>
<link rel="stylesheet" href="https://fonts.googleapis.com/css2?family=EB+Garamond:ital,wght@1,400&family=Marcellus&display=swap">
<style>
  :root {
    --paper: #ffffff;
    --navy: #2b2f97;
    --violet: #7c3aa8;
    --wash-blue: #bcdbe8;
    --wash-lilac: #d7b6e6;
    --water-deep: #3d5fc0;
    --water-light: #dfe8f8;
    --petal: #a7e3e6;
    --bloom: #c23bc9;
  }
  * { margin: 0; padding: 0; box-sizing: border-box; }
  html, body { width: 857px; height: 1200px; overflow: hidden; background: var(--paper); }
  .poster { position: relative; width: 857px; height: 1200px; overflow: hidden; background: var(--paper); }

  .wash { position: absolute; filter: blur(4px); }
  .wash--blue {
    left: -30px; top: -40px; width: 540px; height: 520px;
    border-radius: 38% 46% 52% 40% / 40% 42% 58% 60%;
    background: radial-gradient(ellipse at 45% 40%, var(--wash-blue) 0%, rgba(188,219,232,.7) 55%, rgba(188,219,232,0) 75%);
  }
  .wash--lilac {
    left: 520px; top: -30px; width: 380px; height: 680px;
    border-radius: 50% 30% 40% 60% / 30% 40% 60% 70%;
    background: radial-gradient(ellipse at 55% 40%, var(--wash-lilac) 0%, rgba(215,182,230,.7) 55%, rgba(215,182,230,0) 75%);
  }

  .water {
    position: absolute; left: 0; top: 830px; width: 857px; height: 370px;
    background: linear-gradient(to bottom, rgba(223,232,248,0) 0%, var(--water-light) 12%, #8fa5e0 45%, var(--water-deep) 100%);
  }
  .lotus {
    position: absolute; left: 0; top: 825px; width: 510px; height: 375px;
    background:
      radial-gradient(ellipse 90px 75px at 350px 125px, var(--bloom) 0%, rgba(194,59,201,.5) 45%, rgba(167,227,230,.9) 70%, rgba(167,227,230,0) 100%),
      radial-gradient(ellipse 150px 120px at 180px 240px, var(--bloom) 0%, rgba(194,59,201,.5) 40%, rgba(167,227,230,.9) 65%, rgba(167,227,230,0) 100%);
  }

  .copy { position: absolute; left: 0; top: 0; width: 857px; height: 1200px; }
  .tagline { fill: var(--navy); font-family: "Marcellus", sans-serif; font-size: 33px; }
  .tagline .name { font-family: "EB Garamond", serif; font-style: italic; font-size: 54px; }
  .headline { fill: var(--violet); font-family: "EB Garamond", serif; font-style: italic; font-weight: 400; }
  .headline--lead { font-size: 70px; }
  .headline--name { font-size: 250px; }
</style>
</head>
<body>
<main class="poster">
  <div class="wash wash--blue" role="img" aria-label="Soft blue watercolour wash"></div>
  <div class="wash wash--lilac" role="img" aria-label="Soft lilac watercolour wash"></div>

  <div class="water" role="img" aria-label="Calm blue water surface"></div>
  <div class="lotus" role="img" aria-label="Two turquoise and magenta water lilies floating on the water"></div>

  <svg class="copy" viewBox="0 0 857 1200" width="857" height="1200">
    <text class="tagline" x="11" y="107" textLength="662" lengthAdjust="spacingAndGlyphs"><tspan class="name">Lunae</tspan> for her. <tspan class="name">Lunae</tspan> for him.</text>
    <text class="tagline" x="464" y="253" textLength="325" lengthAdjust="spacingAndGlyphs"><tspan class="name">Lunae</tspan> for you.</text>
    <text class="headline headline--lead" x="240" y="583" textLength="117" lengthAdjust="spacingAndGlyphs">Let’s</text>
    <text class="headline headline--name" x="324" y="790" textLength="456" lengthAdjust="spacingAndGlyphs">Lunae</text>
  </svg>
</main>
</body>
</html>
```